Cyber Security Site Design (Products & Consulting)

I need my website redesigned to be engaging, clean, efficient and modern. My company (when its up and running) is going to be concentrated on two things: a few specific products for cyber security as well as cyber security consulting services. The background I bring to the field is having worked with small companies all the way to the largest government organizations and advising them on their security posture and how to improve it. We need the ability to add products and services easily.

For a sample product, you can use either Tarnel (http://www.tarnel-relay.org/) or Vornidex Graywell (https://www.vornidex.com/products/relay-kx-and-enhanced-safe-portal).

It will replace https://dalmorenvue.com/

Target Market(s)

Cyber Security professionals in all verticals

Coding

Coded - Design and coding required

Number of Pages Required

4 page

Font styles to use
Sans Serif

Colors
6b449b

Requirements
Must have
• Ability to easily modify
• Have main page
• Have product specific pages
• Have consulting services pages
• Have executive team information
• Clean, modern design
• Usage of the logo and its color scheme
Nice to have
• I like the idea of a left collapsed sidebar (so icons only) that can expand for text.
• I am also open to a very unique landing page, possibly a shape in the middle (hexagons maybe?) with each of the options there.
Should not have
• Nothing that looks like it came out of a hacker movie

```html
<!DOCTYPE html>
<html lang="en">
<head>
<meta charset="utf-8">
<title>Dalmoren Vue — Cyber Security Consulting</title>
<link href="https://fonts.googleapis.com/css2?family=Roboto:wght@400;500;700;900&family=Poppins:wght@400;500;600&display=swap" rel="stylesheet">
<style>
:root{
  --stage:#5a2f8a;
  --brand:#6b449b;
  --brand-deep:#4b2a82;
  --ink:#2b2b2b;
  --muted:#6d6d6d;
  --panel-grey:#f0f0f0;
  --lavender:#e7d9f8;
  --navy:#06122e;
  --white:#ffffff;
}
*{box-sizing:border-box;margin:0;padding:0}
html,body{width:769px;height:1200px;overflow:hidden}
body{background:var(--stage);font-family:"Poppins",sans-serif;color:var(--ink);position:relative}
.abs{position:absolute}
.page{position:absolute;left:34px;top:45px;width:342px;height:1110px;background:var(--white);overflow:hidden;box-shadow:0 4px 14px rgba(0,0,0,.25)}
.mobile{position:absolute;left:392px;top:45px;width:343px;height:212px;overflow:hidden;box-shadow:0 4px 14px rgba(0,0,0,.25)}
.heading{font-family:"Roboto",sans-serif;font-weight:700;text-transform:uppercase;line-height:1.15}
.accent{color:var(--brand)}
.pill{position:absolute;border-radius:8px;font-family:"Roboto",sans-serif;font-weight:700;font-size:4.2px;letter-spacing:.2px;text-align:center;text-transform:uppercase;white-space:nowrap}
.pill.outline-light{border:1px solid var(--white);color:var(--white)}
.pill.outline-brand{border:1px solid var(--brand);color:var(--brand)}
.pill.solid{background:var(--brand);color:var(--white)}
.body-copy{font-size:3.7px;line-height:7px;color:var(--muted)}

/* hero */
.hero{position:absolute;left:0;top:0;width:342px;height:217px;background:radial-gradient(circle at 80% 48%,#3fd2ff 0,#1173c9 18%,#0a2f72 45%,#061536 80%)}
.brand-name{position:absolute;font-family:"Poppins",sans-serif;font-weight:500;color:var(--white);letter-spacing:0;display:flex;align-items:center;gap:3px;white-space:nowrap}
.brand-name .dot{display:inline-block;border-radius:50%;background:var(--white)}
.topbar{position:absolute;left:190px;top:11px;font-size:4.8px;color:var(--white);display:flex;align-items:center;gap:3px;white-space:nowrap}
.social{display:inline-block;width:7px;height:7px;border-radius:50%;background:var(--white);opacity:.85}
.main-nav{position:absolute;left:140px;top:27px;display:flex;gap:5px;font-family:"Roboto",sans-serif;font-size:4.3px;font-weight:500;color:var(--white);white-space:nowrap}
.hero-title{position:absolute;left:41px;top:82px;font-size:15.5px;color:var(--white)}
.slider-dots{position:absolute;left:42px;top:148px;display:flex;gap:3px}
.slider-dots span{width:4px;height:4px;border-radius:50%;border:.6px solid var(--white)}
.slider-dots span.on{background:var(--white)}

/* services */
.services{position:absolute;left:0;top:217px;width:342px;height:180px}
.section-title{position:absolute;left:0;width:100%;text-align:center;font-size:10px}
.service{position:absolute;width:66px;text-align:center}
.service svg{display:block;margin:0 auto}
.service h3{font-family:"Roboto",sans-serif;font-weight:500;font-size:6px;margin-top:5px;color:var(--ink)}
.service p{font-size:3.3px;line-height:6.6px;color:var(--muted);margin-top:3px}

/* split rows */
.split{position:absolute;left:0;width:342px;background:var(--panel-grey)}
.split .visual{position:absolute;top:0;height:100%}
.split h2{position:absolute;font-size:10px}
.split .body-copy{position:absolute;width:128px}

/* exec */
.exec{position:absolute;left:0;top:683px;width:342px;height:176px}
.portrait{position:absolute;left:138px;top:24px;width:66px;height:66px;border-radius:50%;border:2px solid var(--brand);background:radial-gradient(circle at 50% 40%,#9aa4b0,#4a5461)}
.arrow{position:absolute;top:81px;width:8px;height:8px;border-radius:50%;background:#8a8a8a}
.exec-title{position:absolute;left:0;top:102px;width:100%;text-align:center;font-size:8px;font-weight:500}
.exec p{position:absolute;left:62px;top:116px;width:218px;text-align:center;font-size:4.2px;line-height:7.5px;color:var(--ink)}
.exec .signature{position:absolute;left:0;top:146px;width:100%;text-align:center;font-size:4.6px;font-weight:500}

/* enquiry */
.enquiry{position:absolute;left:0;top:859px;width:342px;height:166px;background:linear-gradient(180deg,var(--lavender),#dccbf2)}
.field{position:absolute;background:var(--white);border:.5px solid #d8cde6;font-size:3.2px;color:#777;padding:2px 4px}

/* footer */
.site-footer{position:absolute;left:0;top:1025px;width:342px;height:85px;background:var(--white)}
.footer-mark{position:absolute;left:146px;top:-12px;width:50px;height:50px;border-radius:50%;background:var(--white)}
.footer-mark i{position:absolute;left:15px;top:14px;width:20px;height:20px;border-radius:50%;background:var(--brand)}
.footer-links{position:absolute;left:0;width:100%;text-align:center;font-size:4.4px;color:var(--ink);white-space:nowrap}
.footer-copy{position:absolute;left:0;width:100%;text-align:center;font-size:4.2px;color:var(--ink);white-space:nowrap}
.footer-social{position:absolute;left:0;width:100%;display:flex;justify-content:center;gap:4px}
.footer-social span{width:8px;height:8px;border-radius:50%;border:.7px solid var(--brand)}

/* mobile */
.mobile .backdrop{position:absolute;inset:0;background:radial-gradient(ellipse at 50% 85%,#1f4d8c 0,#0b2147 40%,var(--navy) 80%)}
.menu-btn{position:absolute;left:290px;top:13px;width:12px;height:11px;border:1px solid var(--white);border-radius:2px;padding:2px}
.menu-btn i{display:block;height:1px;background:var(--white);margin-bottom:1.5px}
.mobile-title{position:absolute;left:0;top:94px;width:100%;text-align:center;font-size:12.5px;color:var(--white)}
.mobile .footer-links,.mobile .footer-copy{color:var(--white)}
.mobile .footer-social span{border-color:var(--white)}
</style>
</head>
<body>

<main class="page">
  <section class="hero">
    <div class="hero visual" role="img" aria-label="Glowing blue digital padlock on a circuit-board background" style="left:0;top:0"></div>
    <div class="brand-name" style="left:41px;top:18px;font-size:9px"><span class="dot" style="width:11px;height:11px"></span>DALMOREN VUE</div>
    <div class="topbar">
      <svg width="8" height="8" viewBox="0 0 10 10"><circle cx="5" cy="5" r="5" fill="#fff"/><path d="M3 2.6c.4-.3.8-.2 1 .2l.4.9c.1.3 0 .5-.2.7l-.3.3c.3.7.8 1.2 1.5 1.5l.3-.3c.2-.2.4-.3.7-.2l.9.4c.4.2.5.6.2 1l-.4.5c-2.3.2-4.7-2.2-4.5-4.5z" fill="#0a2f72"/></svg>
      <span>Call Us : (555) 0142 7720</span>
      <span class="social"></span><span class="social"></span><span class="social"></span>
    </div>
    <nav class="main-nav"><span>HOME</span><span>PRODUCTS</span><span>CONSULTING</span><span>EXECUTIVE TEAM</span><span>ABOUT</span><span>CONTACT</span></nav>
    <h1 class="heading hero-title">Cyber Security<br>Consulting</h1>
    <div class="pill outline-light" style="left:41px;top:126px;width:53px;height:11px;line-height:9px">Get More Info</div>
    <div class="slider-dots"><span class="on"></span><span></span><span></span></div>
  </section>

  <section class="services">
    <h2 class="heading section-title" style="top:40px">Our <span class="accent">Services</span></h2>
    <div class="service" style="left:32px;top:66px">
      <svg width="46" height="46" viewBox="0 0 46 46"><rect x="8" y="8" width="30" height="30" transform="rotate(45 23 23)" fill="var(--brand)" stroke="#222" stroke-width="1"/><rect x="15" y="17" width="16" height="11" fill="none" stroke="#fff" stroke-width="1"/><rect x="20" y="22" width="6" height="5" fill="#fff"/><path d="M21 22v-2a2 2 0 0 1 4 0v2" fill="none" stroke="#fff"/></svg>
      <h3>Cyber Security</h3>
      <p>Sed ut perspiciatis unde omnis iste natus error sit voluptatem santium doloremque dantium, totam rem aperiam</p>
    </div>
    <div class="service" style="left:102px;top:66px">
      <svg width="46" height="46" viewBox="0 0 46 46"><rect x="8" y="8" width="30" height="30" transform="rotate(45 23 23)" fill="var(--brand)" stroke="#222" stroke-width="1"/><circle cx="23" cy="17" r="3" fill="none" stroke="#fff"/><circle cx="16" cy="27" r="2.5" fill="none" stroke="#fff"/><circle cx="30" cy="27" r="2.5" fill="none" stroke="#fff"/><path d="M23 20v3M18 26l5-3 5 3" fill="none" stroke="#fff"/></svg>
      <h3>Consulting</h3>
      <p>Sed ut perspiciatis unde omnis iste natus error sit voluptatem santium doloremque dantium, totam rem aperiam</p>
    </div>
    <div class="service" style="left:173px;top:66px">
      <svg width="46" height="46" viewBox="0 0 46 46"><rect x="8" y="8" width="30" height="30" transform="rotate(45 23 23)" fill="var(--brand)" stroke="#222" stroke-width="1"/><circle cx="24" cy="22" r="6" fill="none" stroke="#fff"/><path d="M24 18v8M16 30l4-4" stroke="#fff" fill="none"/></svg>
      <h3>Nemo enim ips</h3>
      <p>Sed ut perspiciatis unde omnis iste natus error sit voluptatem santium doloremque dantium, totam rem aperiam</p>
    </div>
    <div class="service" style="left:244px;top:66px">
      <svg width="46" height="46" viewBox="0 0 46 46"><rect x="8" y="8" width="30" height="30" transform="rotate(45 23 23)" fill="var(--brand)" stroke="#222" stroke-width="1"/><rect x="15" y="16" width="16" height="11" fill="none" stroke="#fff"/><path d="M20 30h6M23 27v3" stroke="#fff"/><circle cx="23" cy="21.5" r="2.5" fill="#fff"/></svg>
      <h3>Quis autem vel</h3>
      <p>Sed ut perspiciatis unde omnis iste natus error sit voluptatem santium doloremque dantium, totam rem aperiam</p>
    </div>
  </section>

  <section class="split" style="top:397px;height:139px">
    <div class="visual" role="img" aria-label="Security team working at monitors in an operations room" style="left:0;width:167px;background:linear-gradient(135deg,#2c3e5c,#0f1b2e 60%,#3a4e6e)"></div>
    <h2 class="heading" style="left:183px;top:28px">Welcome to<br><span class="accent">Dalmoren Vue</span></h2>
    <p class="body-copy" style="left:183px;top:56px">Lorem ipsum dolor sit amet, consectetur adipiscing elit, sed do eiusmod tempor incididunt ut labore et dolore magna aliqua. Ut enim ad minim veniam, quis nostrud exercitation ullamco laboris nisi ut aliquip ex ea commodo consequat.</p>
    <div class="pill outline-brand" style="left:183px;top:102px;width:43px;height:10px;line-height:8px">Read More</div>
  </section>

  <section class="split" style="top:536px;height:147px">
    <h2 class="heading" style="left:40px;top:30px">Products<br><span class="accent">Cyber Security</span></h2>
    <p class="body-copy" style="left:40px;top:58px">Lorem ipsum dolor sit amet, consectetur adipiscing elit, sed do eiusmod tempor incididunt ut labore et dolore magna aliqua. Ut enim ad minim veniam, quis nostrud exercitation ullamco laboris nisi ut aliquip ex ea commodo consequat.</p>
    <div class="pill outline-brand" style="left:41px;top:104px;width:43px;height:10px;line-height:8px">Read More</div>
    <div class="visual" role="img" aria-label="Hand touching a glowing padlock on a digital security interface" style="left:176px;width:166px;background:radial-gradient(circle at 75% 55%,#ff7a2a 0,#8a3a2a 16%,#1a2f55 45%,#0a1630 90%)"></div>
  </section>

  <section class="exec">
    <div class="portrait" role="img" aria-label="Portrait of the executive team member"></div>
    <span class="arrow" style="left:34px"></span>
    <span class="arrow" style="left:300px"></span>
    <h2 class="heading exec-title">Executive Team</h2>
    <p>Sed ut perspiciatis unde omnis iste natus error sit voluptatem accusantium doloremque laudantium, totam rem aperiam, eaque ipsa quae ab illo inventore veritatis et quasi architecto beatae vitae dicta sunt explicabo. Nemo enim ipsam voluptatem quia voluptas sit aspernatur</p>
    <div class="signature">Marcus Hale, Dalmoren Vue</div>
  </section>

  <section class="enquiry">
    <h2 class="heading section-title" style="top:27px;font-size:10px;font-weight:500">Send an Enquiry</h2>
    <div class="field" style="left:71px;top:51px;width:96px;height:11px">Name</div>
    <div class="field" style="left:173px;top:51px;width:96px;height:11px">Phone</div>
    <div class="field" style="left:71px;top:68px;width:96px;height:11px">Email</div>
    <div class="field" style="left:173px;top:68px;width:96px;height:11px">Subject</div>
    <div class="field" style="left:71px;top:85px;width:198px;height:24px">Message</div>
    <div class="pill solid" style="left:141px;top:120px;width:57px;height:12px;line-height:12px;border-radius:6px">Send Messages</div>
  </section>

  <footer class="site-footer">
    <div class="footer-mark"><i></i></div>
    <div class="footer-links" style="top:38px">Home &nbsp;|&nbsp; About Us &nbsp;|&nbsp; Products &nbsp;|&nbsp; Consulting &nbsp;|&nbsp; Executive Tea &nbsp;|&nbsp; Contact</div>
    <div class="footer-copy" style="top:50px">Dalmoren Vue, LLC © 2018 All Rights Reserved.</div>
    <div class="footer-social" style="top:62px"><span></span><span></span><span></span></div>
  </footer>
</main>

<aside class="mobile">
  <div class="backdrop" role="img" aria-label="Dark blue digital hexagon network mesh"></div>
  <div class="menu-btn"><i></i><i></i><i></i></div>
  <div class="brand-name" style="left:128px;top:50px;font-size:9px"><span class="dot" style="width:11px;height:11px"></span>DALMOREN VUE</div>
  <div class="abs" style="left:146px;top:82px;width:50px;height:2px;background:#3b8ee8"></div>
  <h1 class="heading mobile-title">Cyber Security Consulting</h1>
  <div class="pill solid" style="left:145px;top:117px;width:53px;height:11px;line-height:11px">Get More Info</div>
  <div class="footer-links" style="top:171px;font-size:4.2px">Home &nbsp;|&nbsp; About Us &nbsp;|&nbsp; Products &nbsp;|&nbsp; Consulting &nbsp;|&nbsp; Executive Tea &nbsp;|&nbsp; Contact</div>
  <div class="footer-copy" style="top:183px">Dalmoren Vue, LLC © 2018 All Rights Reserved.</div>
  <div class="footer-social" style="top:196px"><span></span><span></span><span></span></div>
</aside>

</body>
</html>
```